Christmas Web Slider

We need a new clean and quality Christmas Slider for our home page (https://www.plumvalehome.co.uk/) to engage customers to interact with our Christmas ranges. It will link to our All Christmas Products department page. Must be within the specs of our current sliders for size and be minimal in memory size to avoid slowing the web page load time down.

Target Market(s)

home and business users but more home public for this product category

Industry/Entity Type

artificial Christmas trees and related Chirtmas products and decor

Colors
00AB8E
00BBA5
67D7C9
C6EFE9
E9F9F6
FFC000
F8CF3A
FAE287
FDF2CF
FEFAEE
EB3D1F
EC4F4E
F09395
F8D3D4
FCEDEE

Requirements
Must have
• typical festive imagery and text to engage and draw the visitor in to click
Nice to have
• obvious call to actions
Should not have
• anyhting cheap or tacky

```html
<!DOCTYPE html>
<html lang="en">
<head>
<meta charset="utf-8">
<title>Christmas Web Slider – Presentation Sheet</title>
<link rel="stylesheet" href="https://fonts.googleapis.com/css2?family=Cookie&family=Montserrat:wght@500;600;700;800&family=Questrial&display=swap">
<style>
  :root {
    --page-bg: #f5f5f5;
    --title-green: #11980f;
    --size-red: #e8202a;
    --sky-deep: #1d6c78;
    --sky-mid: #7fb8bc;
    --sky-light: #dff0ee;
    --snow: #fbfbfb;
    --headline-red: #ff0a0a;
    --script-white: #ffffff;
    --tagline-green: #0c9a12;
    --sub-teal: #0e6b5a;
    --button-teal: #08755f;
    --button-text: #ffffff;
  }

  * { margin: 0; padding: 0; box-sizing: border-box; }

  html, body {
    width: 1200px;
    height: 870px;
    overflow: hidden;
    background: var(--page-bg);
  }

  .sheet {
    position: relative;
    width: 1200px;
    height: 870px;
  }

  .sheet-title {
    position: absolute;
    top: 82px;
    left: 0;
    width: 100%;
    text-align: center;
    font-family: "Montserrat", sans-serif;
    font-weight: 600;
    font-size: 35px;
    color: var(--title-green);
    letter-spacing: 0.3px;
  }

  .sheet-size {
    position: absolute;
    top: 141px;
    left: 0;
    width: 100%;
    text-align: center;
    font-family: "Montserrat", sans-serif;
    font-weight: 500;
    font-size: 25px;
    color: var(--size-red);
  }

  .slider {
    position: absolute;
    left: 40px;
    top: 205px;
    width: 1104px;
    height: 552px;
    overflow: hidden;
    box-shadow: 0 1px 6px rgba(0, 0, 0, 0.18);
    background:
      linear-gradient(180deg, rgba(251,251,251,0) 0%, rgba(251,251,251,0) 64%, var(--snow) 74%, var(--snow) 100%),
      radial-gradient(ellipse 60% 55% at 70% 60%, #f4fbf9 0%, rgba(244,251,249,0) 70%),
      linear-gradient(120deg, var(--sky-deep) 0%, var(--sky-mid) 35%, var(--sky-light) 70%, #e9f6f4 100%);
  }

  .slider-visual {
    position: absolute;
    left: 64px;
    top: 21px;
    width: 368px;
    height: 531px;
    border-radius: 46% 46% 6px 6px / 70% 70% 6px 6px;
    background: linear-gradient(180deg, #e0b444 0%, #2f7d2c 18%, #2f7d2c 50%, #c23a2e 70%, #d8d4cf 100%);
    opacity: 0.9;
  }

  .slider-copy {
    position: absolute;
    left: 392px;
    top: 0;
    width: 720px;
    height: 100%;
    text-align: center;
  }

  .headline-script {
    position: absolute;
    top: 70px;
    left: 0;
    width: 100%;
    font-family: "Cookie", cursive;
    font-size: 168px;
    line-height: 1;
    color: var(--script-white);
    -webkit-text-stroke: 10px var(--headline-red);
    paint-order: stroke fill;
    transform: scaleX(1.12);
    z-index: 2;
  }

  .headline-main {
    position: absolute;
    top: 198px;
    left: 0;
    width: 100%;
    font-family: "Montserrat", sans-serif;
    font-weight: 700;
    font-size: 108px;
    line-height: 1;
    letter-spacing: -2px;
    color: var(--headline-red);
    text-shadow: 2px 4px 6px rgba(80, 20, 20, 0.35);
    transform: scaleY(1.08);
    transform-origin: top center;
    z-index: 1;
  }

  .tagline {
    position: absolute;
    top: 330px;
    left: 0;
    width: 100%;
    font-family: "Questrial", sans-serif;
    font-size: 37px;
    letter-spacing: 2px;
    color: var(--tagline-green);
    -webkit-text-stroke: 0.6px var(--tagline-green);
  }

  .subline {
    position: absolute;
    top: 386px;
    left: 0;
    width: 100%;
    font-family: "Montserrat", sans-serif;
    font-weight: 700;
    font-size: 22px;
    letter-spacing: 3px;
    color: var(--sub-teal);
  }

  .cta-button {
    position: absolute;
    top: 452px;
    left: 240px;
    width: 240px;
    height: 51px;
    background: var(--button-teal);
    color: var(--button-text);
    font-family: "Questrial", sans-serif;
    font-size: 25px;
    letter-spacing: 1px;
    line-height: 51px;
    text-decoration: none;
    display: block;
  }
</style>
</head>
<body>
  <main class="sheet">
    <h1 class="sheet-title">Web Slider Banner – Mockup 4 – Revision 4c</h1>
    <p class="sheet-size">Size:1240px(width) X 620px(height)</p>

    <section class="slider">
      <div class="slider-visual" role="img" aria-label="Decorated Christmas tree with a gold star, surrounded by a pile of wrapped gifts in red, gold, white and silver"></div>

      <div class="slider-copy">
        <p class="headline-script">Happy</p>
        <h2 class="headline-main">CHRISTMAS</h2>
        <p class="tagline">SALE IS ON. BUY YOUR GIFTS</p>
        <p class="subline">TREE, GIFTS &amp; DECOR</p>
        <a class="cta-button" href="#all-christmas">SHOP NOW</a>
      </div>
    </section>
  </main>
</body>
</html>
```